Thornwick Estates Managment Ltd website

Need a website To inform people/clients of the services we provide. 5 pages total with a local feel. Bristol, UK. I have logo artwork already is like the look based on
incorporate the artwork attached for theme, feel and colours fonts info etc

To best describe the business have a brief look at www.fernbaylettings.co.uk which is a local firm offering the same services. This is for your ref only and not to be copied.

Target Market(s)

Property Investors/Landlords

Coding

Coded - Design and coding required

Number of Pages Required

5+ page

Colors
0392cd
f68d4d

Requirements
Must have
• local feel. Possibly using some local architecture or historic landmarks etc. This is fexible.
• most also be mobile device compatible
Nice to have
• the membership logos - files attached: KTB, GHW, DVT and safebondhold.co.uk

```html
<!DOCTYPE html>
<html lang="en">
<head>
<meta charset="utf-8">
<title>Thornwick Estates Managment Ltd</title>
<link href="https://fonts.googleapis.com/css2?family=Questrial&family=Ubuntu:wght@500&family=Fira+Sans+Condensed&display=swap" rel="stylesheet">
<style>
:root{
  --orange:#ff7f00;
  --orange-line:#c86000;
  --teal:#3f9a9c;
  --teal-dark:#1f4f55;
  --page-dark:#2b2a37;
  --panel:#e6e6e6;
  --ink:#1d1d1d;
  --muted:#777;
  --white:#fff;
}
*{margin:0;padding:0;box-sizing:border-box}
html,body{width:1024px;height:1200px;overflow:hidden}
body{
  position:relative;
  background:linear-gradient(to bottom,#e7e7e7 0,#cfcfd3 569px,var(--page-dark) 569px);
  font-family:Arial,Helvetica,sans-serif;
}
.brand{position:absolute;top:58px;left:0;width:1024px;display:flex;justify-content:center;align-items:center;gap:14px}
.brand-mark{width:40px;height:40px;background:var(--teal)}
.brand-name{font-family:'Ubuntu',sans-serif;font-weight:500;font-size:44px;color:var(--teal-dark);letter-spacing:-.5px}
.hero{position:absolute;left:66px;top:133px;width:892px;height:436px;
  background:linear-gradient(to bottom,#1f2a3a 0%,#394252 35%,#5a5550 60%,#7a7d72 80%,#b9b9b4 100%)}
.hero-title{position:absolute;top:350px;left:66px;width:892px;text-align:center;color:var(--white);
  font:bold 39px Arial,Helvetica,sans-serif;letter-spacing:.3px;text-shadow:0 1px 3px rgba(0,0,0,.4)}
.hero-tagline{position:absolute;top:405px;left:66px;width:892px;text-align:center;color:var(--white);
  font-family:'Fira Sans Condensed',sans-serif;font-size:17px;letter-spacing:1.6px}
.hero-arrow{position:absolute;top:338px;width:58px;height:53px;background:var(--orange);color:var(--white);
  font:bold 26px Arial,sans-serif;display:flex;align-items:center;justify-content:center}
.hero-arrow.prev{left:66px}.hero-arrow.next{left:900px}
.main-nav{position:absolute;left:66px;top:569px;width:892px;height:71px;background:var(--orange);
  display:flex;justify-content:center;font-family:'Questrial',sans-serif;font-size:14px}
.main-nav a{color:var(--ink);text-decoration:none;display:flex;align-items:center;padding:0 18px;border-left:1px solid var(--orange-line)}
.main-nav a:first-child{border-left:none;color:var(--white);font-size:15px;padding:0 22px}
.content{position:absolute;left:66px;top:640px;width:892px;height:396px;background:var(--panel)}
.welcome{text-align:center;margin-top:46px;font-family:'Questrial',sans-serif;font-size:31px;font-weight:400;color:var(--ink)}
.welcome span{color:var(--orange)}
.intro{width:736px;margin:22px auto 0;text-align:center;font-size:14px;line-height:26.6px;color:#222}
.divider{position:absolute;left:21px;top:221px;width:850px;height:1px;background:#b5b5b5}
.service{position:absolute;top:265px;width:290px}
.service svg{position:absolute;left:9px;top:2px}
.service h3{margin-left:80px;font-family:'Questrial',sans-serif;font-weight:400;font-size:16.5px;color:var(--ink)}
.service p{margin-left:80px;margin-top:8px;width:200px;font-size:12.4px;line-height:20px;color:var(--muted)}
.site-footer{position:absolute;left:66px;top:1036px;width:892px;height:164px;background:var(--orange);color:var(--white);font-size:12.4px}
.contact{position:absolute;top:34px;display:flex;gap:10px;line-height:19px}
.social{position:absolute;right:26px;top:52px;display:flex;gap:14px}
.social span{width:10px;height:10px;border-radius:50%;background:#3a2a1a}
.footer-rule{position:absolute;left:21px;top:97px;width:850px;height:1px;background:var(--orange-line)}
.copyright{position:absolute;top:124px;width:100%;text-align:center;font-size:12.4px}
.copyright b{font-weight:400;color:var(--ink)}
</style>
</head>
<body>
<header class="brand">
  <span class="brand-mark"></span>
  <span class="brand-name">Thornwick</span>
</header>

<section class="hero" role="img" aria-label="Photograph of a modern detached family house with hedges and a garage at dusk"></section>
<h1 class="hero-title">Thornwick Estates Managements ltd</h1>
<p class="hero-tagline">THE PERFECT SOLUTION FOR LANDLORDS, TENANTS &amp; AGENCIES IN BRISTOL</p>
<div class="hero-arrow prev">&laquo;</div>
<div class="hero-arrow next">&raquo;</div>

<nav class="main-nav">
  <a href="#">Home</a><a href="#">About Us</a><a href="#">Services</a><a href="#">Agencies</a><a href="#">Contact Us</a>
</nav>

<main class="content">
  <h2 class="welcome">Welcome To <span>Thornwick</span></h2>
  <p class="intro">Lorem ipsum dolor sit amet, consectetur adipiscing elit, sed do eiusmod tempor incididunt ut labore et dolore magna aliqua. Ut enim ad minim veniam, quis nostrud exercitation ullamco laboris nisi ut aliquip ex ea commodo consequat. Duis aute irure dolor in reprehenderit in voluptate velit esse cillum dolore eu fugiat nulla pariatur.</p>
  <div class="divider"></div>

  <article class="service" style="left:21px">
    <svg width="44" height="44" viewBox="0 0 44 44"><path d="M22 4 L40 20 L35 20 L35 40 L9 40 L9 20 L4 20 Z" fill="var(--teal)"/><rect x="18" y="27" width="8" height="13" fill="var(--panel)"/></svg>
    <h3>FOR LANDLORDS</h3>
    <p>Lorem ipsum dolor sit amet, consectetur adipiscing elit, sed do eiusmod.</p>
  </article>
  <article class="service" style="left:305px">
    <svg width="44" height="44" viewBox="0 0 44 44" fill="var(--teal)"><circle cx="22" cy="13" r="9"/><path d="M5 42 C5 29 39 29 39 42 Z"/></svg>
    <h3>FOR TENANTS</h3>
    <p>Lorem ipsum dolor sit amet, consectetur adipiscing elit, sed do eiusmod.</p>
  </article>
  <article class="service" style="left:595px">
    <svg width="44" height="44" viewBox="0 0 44 44" fill="var(--teal)"><rect x="15" y="6" width="14" height="8" rx="2" fill="none" stroke="var(--teal)" stroke-width="3"/><rect x="4" y="13" width="36" height="27" rx="3"/><rect x="4" y="24" width="36" height="2" fill="var(--panel)"/></svg>
    <h3>FOR AGENCIES</h3>
    <p>Lorem ipsum dolor sit amet, consectetur adipiscing elit, sed do eiusmod.</p>
  </article>
</main>

<footer class="site-footer">
  <div class="contact" style="left:26px">
    <svg width="12" height="17" viewBox="0 0 12 17"><path d="M6 0a6 6 0 0 1 6 6c0 4-6 11-6 11S0 10 0 6a6 6 0 0 1 6-6z" fill="var(--white)"/><circle cx="6" cy="6" r="2.2" fill="var(--orange)"/></svg>
    <span>14 Harlow Lane, Eastfold,<br>Marbury, MB4 9QX</span>
  </div>
  <div class="contact" style="left:230px">
    <svg width="11" height="18" viewBox="0 0 11 18"><rect x="1" y="1" width="9" height="16" rx="2" fill="none" stroke="var(--white)" stroke-width="2"/><rect x="4" y="13" width="3" height="1.5" fill="var(--white)"/></svg>
    <span>0100 000 4271</span>
  </div>
  <div class="contact" style="left:368px">
    <svg width="14" height="12" viewBox="0 0 14 12" style="margin-top:4px"><rect width="14" height="10" rx="1" fill="var(--white)"/><path d="M0 1 L7 6 L14 1" stroke="var(--orange)" stroke-width="1.4" fill="none"/></svg>
    <span style="margin-left:6px">info@thornwickestates.co.uk</span>
  </div>
  <div class="social"><span></span><span></span><span></span></div>
  <div class="footer-rule"></div>
  <p class="copyright">&copy; <b>Thornwick</b> - 2016. All Rights Resrevd.</p>
</footer>
</body>
</html>
```